Upmarket Bathroom and Kitchen ware supplier needs a classy business card design

We are a company based in Fiji, we sell plumbing ware (Kitchen and bathroom taps, Basins,showers, toilets etc) through up market show rooms to individuals and directly through Architects and designers of resorts and holiday houses for new builds and renovations. we are wanting to upgrade our over all look and brand. we are starting with a new logo but will be rebranding the whole business. This project is for a business card design for my management and tales team I would like it to be dark, classy and interesting

Target Market(s)

Resort directors and Management, High end holiday home owners

Contact Information for Business Card

Neil Dawson
Director
+64219473815

Colors

Designer to choose colors to be used in the design.

Requirements
Must have
• Must have an upmarket appearance I like darker charcoal shades but will be guided by the designers
• Please any catch phrases like "Crafting remarkable living rooms" this belongs tpo one of our suppliers so can not be used.
Nice to have
• Double sided, so front dedicated to logo provided and back info about the business and the person.

```html
<!DOCTYPE html>
<html lang="en">
<head>
<meta charset="utf-8">
<title>Lagoon Interiors – Business Card</title>
<link rel="stylesheet" href="https://fonts.googleapis.com/css2?family=Jost:wght@300;400;700&display=swap">
<style>
  :root {
    --page: #ffffff;
    --ink: #000000;
    --paper: #ffffff;
    --band-grey: #c3c3c3;
    --band-dark: #070909;
    --card-edge: #555555;
  }
  * { margin: 0; padding: 0; box-sizing: border-box; }
  html, body {
    width: 1200px; height: 1200px; overflow: hidden;
    background: var(--page);
    font-family: "Jost", sans-serif;
  }
  .canvas { position: relative; width: 1200px; height: 1200px; }
  .card { position: absolute; left: 140px; width: 919px; height: 525px; overflow: hidden; }
  .card svg.decor { position: absolute; inset: 0; width: 100%; height: 100%; }
  .card-front { top: 56px; background: var(--ink); }
  .card-back { top: 619px; background: var(--paper); border: 1px solid var(--card-edge); }

  .wordmark {
    position: absolute; text-align: center; font-weight: 300; line-height: 1;
    -webkit-font-smoothing: antialiased;
  }
  .wordmark .name { display: block; text-transform: uppercase; }
  .wordmark .sub { display: block; text-transform: uppercase; }

  .card-front .wordmark { left: 0; right: 0; top: 228px; color: var(--paper); }
  .card-front .wordmark .name { font-size: 40px; letter-spacing: 14px; padding-left: 14px; }
  .card-front .wordmark .sub { font-size: 14px; letter-spacing: 8px; padding-left: 8px; margin-top: 14px; }

  .card-back .wordmark { left: 40px; width: 290px; top: 312px; color: var(--ink); }
  .card-back .wordmark .name { font-size: 24px; letter-spacing: 9px; padding-left: 9px; }
  .card-back .wordmark .sub { font-size: 10px; letter-spacing: 5px; padding-left: 5px; margin-top: 10px; }

  .contact { position: absolute; left: 316px; top: 188px; color: var(--ink); line-height: 1; }
  .contact .person { font-size: 47px; font-weight: 700; letter-spacing: 1px; text-transform: uppercase; white-space: nowrap; }
  .contact .role { font-size: 36px; font-weight: 400; margin-top: 26px; }
  .contact .phone { font-size: 36px; font-weight: 400; margin-top: 12px; letter-spacing: 1px; }
</style>
</head>
<body>
<main class="canvas">

  <section class="card card-front">
    <svg class="decor" viewBox="0 0 1480 845" preserveAspectRatio="none" aria-hidden="true">
      <polygon points="1242,845 1302,845 1480,668 1480,608" fill="#ffffff"/>
    </svg>
    <div class="wordmark">
      <span class="name">Lagoon</span>
      <span class="sub">Interiors</span>
    </div>
  </section>

  <section class="card card-back">
    <svg class="decor" viewBox="0 0 1480 845" preserveAspectRatio="none" aria-hidden="true">
      <polygon points="141,0 194,0 0,194 0,140" fill="#070909"/>
      <polygon points="817,845 921,845 1480,289 1480,184" fill="#c3c3c3"/>
    </svg>
    <div class="wordmark">
      <span class="name">Lagoon</span>
      <span class="sub">Interiors</span>
    </div>
    <div class="contact">
      <p class="person">Rowan Kettering</p>
      <p class="role">Director</p>
      <p class="phone">+64219473815</p>
    </div>
  </section>

</main>
</body>
</html>
```